Counseling Practice Business Card

I need a professional looking business card incorporating my new logo that was just completed. Card needs to incorporate my name and title, description of my specialty, my address, my phone number, my fax number, my email and my website URL. I need to be able to choose design on/with different paper colors and textures.
I do not have a lot of business card ideas so I am open to anything but I want bold,sharp, clear card without additional designs other than my logo (see attached file info). I am open to different color backgrounds or paper colors including black. I do not like traditional brackets around area codes in phone number or dashes between numbers in phone number. Am open to other ways of presenting including periods between numbers as appropriate. I do not know enough to know what I like yet but I want card to coordinate and work together with my logo. My practice emphasizes natural mental health interventions so any use of color (with background paper color or the blue and green in my logo) that elicits nature is nice. In addition to black, any natural brown or wood looking background might be desirable also. Most of the offerings so far look very similar and boring.

Target Market(s)

Potential therapy clients and other professionals

Contact Information for Business Card

Card information:
Marcus T. Whitfield, Ph.D.
Licensed Clinical Psychologist
Integrative Health Coach
4812 Ferndale Pkwy NW
Suite 730
Duluth, GA 30096
(770) 555-0142 phone
(770) 555-0186 fax
drmarcuswhitfield@kelvora.com
pathbloomcounseling.com

Font styles to use
Serif
Sans Serif
Other font styles liked:
• anything that you think looks crisp, clear and easily readable

Requirements
Must have
• Any color used should coordinate with my logo design (see attached files).
• Card should be printed horizontally so top and bottom are longest sides of rectangle.
• Background color or paper color should complement and highlight logo. Do not like a white background. black, grey, brown or any color my logo would blend well with.
Nice to have
• I would like designer to utilize color to highlight letters/name or phone-fax-web symbols.
• Bottom edge of card could be highlighted if appropriate to an idea.
Should not have
• I would NOT want the card to have a pure white background at all.
• No clear cards.
• Cards should be oriented with long sides on bottom and top, NOT sides. DO NOT LIKE THIS THIN TALL ORIENTATION.

```html
<!DOCTYPE html>
<html lang="en">
<head>
<meta charset="utf-8">
<title>Pathbloom Counseling – Business Card</title>
<link rel="stylesheet" href="https://fonts.googleapis.com/css2?family=EB+Garamond:wght@400;600&display=swap">
<style>
  :root {
    --page: #ffffff;
    --card-edge: #1f272e;
    --card-face: #121619;
    --brand-blue: #3b87e0;
    --brand-green: #137a12;
    --contact-text: #eadbd6;
  }
  * { margin: 0; padding: 0; box-sizing: border-box; }
  html, body {
    width: 1200px; height: 788px; overflow: hidden;
    background: var(--page);
  }
  .canvas { position: relative; width: 1200px; height: 788px; }
  .card {
    position: absolute; left: 124px; top: 119px;
    width: 949px; height: 543px;
    background: var(--card-edge);
    overflow: hidden;
    font-family: "EB Garamond", Georgia, serif;
  }
  .card-face {
    position: absolute; left: 12px; top: 12px; right: 12px; bottom: 0;
    background: var(--card-face);
  }
  .card-wave { position: absolute; left: 0; top: 0; width: 949px; height: 543px; }
  .identity {
    position: absolute; right: 42px; top: 64px;
    text-align: right; font-weight: 600; line-height: 1;
  }
  .identity-name { color: var(--brand-blue); font-size: 37px; }
  .identity-title { color: var(--brand-green); font-size: 32px; margin-top: 12px; }
  .practice-name {
    position: absolute; left: 56px; top: 262px;
    color: var(--brand-blue); font-weight: 600; line-height: 1.05;
  }
  .practice-name .primary { display: block; font-size: 64px; }
  .practice-name .secondary { display: block; font-size: 27px; letter-spacing: 0.42em; margin-top: 6px; }
  .contact-list { position: absolute; left: 524px; top: 238px; list-style: none; }
  .contact-item {
    display: flex; align-items: center;
    color: var(--contact-text); font-size: 25px; line-height: 31px;
    margin-bottom: 16px;
  }
  .contact-item:last-child { margin-bottom: 0; }
  .contact-icon { flex: none; width: 34px; height: 34px; margin-right: 16px; }
</style>
</head>
<body>
<div class="canvas">
  <div class="card">
    <div class="card-face"></div>
    <svg class="card-wave" viewBox="0 0 949 543" aria-hidden="true">
      <path d="M0 466 C250 452 500 510 700 530 C820 540 900 515 949 488 L949 543 L0 543 Z" fill="var(--brand-blue)"/>
      <path d="M0 482 C250 470 500 518 700 538 C820 548 900 520 949 490 L949 543 L0 543 Z" fill="var(--brand-green)"/>
    </svg>

    <div class="identity">
      <div class="identity-name">Marcus T. Whitfield, Ph.D.</div>
      <div class="identity-title">Licensed Clinical Psychologist/ Integrative Health Coach</div>
    </div>

    <div class="practice-name">
      <span class="primary">Pathbloom</span>
      <span class="secondary">COUNSELING</span>
    </div>

    <ul class="contact-list">
      <li class="contact-item">
        <svg class="contact-icon" viewBox="0 0 34 34" aria-hidden="true">
          <circle cx="17" cy="17" r="17" fill="var(--brand-blue)"/>
          <path d="M17 7a6 6 0 0 0-6 6c0 5 6 13 6 13s6-8 6-13a6 6 0 0 0-6-6z" fill="var(--brand-green)"/>
          <circle cx="17" cy="13" r="2.2" fill="var(--brand-blue)"/>
        </svg>
        <span>4812 Ferndale Pkwy NW<br>Suite 730, Duluth, GA 30096</span>
      </li>
      <li class="contact-item">
        <svg class="contact-icon" viewBox="0 0 34 34" aria-hidden="true">
          <circle cx="17" cy="17" r="17" fill="var(--brand-blue)"/>
          <g fill="none" stroke="var(--brand-green)" stroke-width="1.8">
            <circle cx="17" cy="17" r="8"/>
            <ellipse cx="17" cy="17" rx="3.5" ry="8"/>
            <path d="M9 17h16M10.5 13h13M10.5 21h13"/>
          </g>
        </svg>
        <span>pathbloomcounseling.com</span>
      </li>
      <li class="contact-item">
        <svg class="contact-icon" viewBox="0 0 34 34" aria-hidden="true">
          <circle cx="17" cy="17" r="17" fill="var(--brand-blue)"/>
          <rect x="9" y="11" width="16" height="12" fill="var(--brand-green)"/>
          <path d="M9 11l8 7 8-7" fill="none" stroke="var(--brand-blue)" stroke-width="1.6"/>
        </svg>
        <span>drmarcuswhitfield@kelvora.com</span>
      </li>
      <li class="contact-item">
        <svg class="contact-icon" viewBox="0 0 34 34" aria-hidden="true">
          <circle cx="17" cy="17" r="17" fill="var(--brand-blue)"/>
          <rect x="12" y="8" width="10" height="6" fill="var(--brand-green)"/>
          <rect x="9" y="14" width="16" height="9" rx="1.5" fill="var(--brand-green)"/>
          <rect x="12" y="20" width="10" height="6" fill="var(--brand-green)" stroke="var(--brand-blue)" stroke-width="1"/>
        </svg>
        <span>(770) 555-0186</span>
      </li>
      <li class="contact-item">
        <svg class="contact-icon" viewBox="0 0 34 34" aria-hidden="true">
          <circle cx="17" cy="17" r="17" fill="var(--brand-blue)"/>
          <path d="M12 8l3.5 0 1.5 5-2.2 1.6a11 11 0 0 0 4.6 4.6L21 17l5 1.5V22a2 2 0 0 1-2 2C15.5 24 10 18.5 10 10a2 2 0 0 1 2-2z" fill="var(--brand-green)"/>
        </svg>
        <span>(770) 555-0142</span>
      </li>
    </ul>
  </div>
</div>
</body>
</html>
```